" A empresa Palkoro nasceu para suprir a necessidade do mercado de empresas em TI que prestem um serviço diferenciado e de qualidade. Além disso, a ideia da Palkoro é ser parceira dos seus clientes e sempre buscar sanar em sua totalidade a necessidades dos seus clientes mesmo que seja através de uma terceira empresa. Como produtos a empresa irá vender soluçoes em TI ( Antivirus, firewall, hospedagens, etc..), projetos e consultoria em TI. "

```html
<!DOCTYPE html>
<html lang="pt-BR">
<head>
<meta charset="utf-8">
<title>Palkoro – Papelaria</title>
<link href="https://fonts.googleapis.com/css2?family=Roboto+Condensed:wght@400;700;800&display=swap" rel="stylesheet">
<style>
  :root{
    --orange:#f6a81e;
    --orange-light:#fbc54f;
    --gray:#7d7e80;
    --gray-dark:#6a6b6d;
    --gray-text:#8a8b8d;
    --watermark:#ececec;
    --paper:#ffffff;
    --bg:#ffffff;
    --label:#222222;
  }
  *{box-sizing:border-box;margin:0;padding:0}
  html,body{width:1200px;height:1200px;overflow:hidden;background:var(--bg)}
  body{position:relative;font-family:"Roboto Condensed",Arial,sans-serif}

  .wordmark{font-family:"Roboto Condensed",Arial,sans-serif;font-weight:800;color:var(--gray);letter-spacing:-1px;line-height:1;text-transform:uppercase}
  .tagline{font-weight:700;color:var(--gray);text-transform:uppercase;letter-spacing:.2px}
  .services{list-style:none;color:var(--gray-text);text-transform:uppercase}
  .services li{display:flex;align-items:center}
  .services svg{flex:none}

  /* Letterhead */
  .letterhead{position:absolute;left:12px;top:12px;width:821px;height:1111px;background:var(--paper);border:1px solid #dcdcdc;overflow:hidden}
  .letterhead__top-band{position:absolute;left:0;top:0;width:100%;height:9px;background:var(--orange)}
  .letterhead .wordmark{position:absolute;left:96px;top:82px;font-size:78px}
  .letterhead .tagline{position:absolute;left:98px;top:164px;font-size:14.5px}
  .letterhead .services{position:absolute;left:564px;top:92px;font-size:17px;line-height:21px}
  .letterhead .services svg{width:14px;height:14px;margin-right:7px}
  .letterhead__watermark{position:absolute;left:250px;top:700px;font-size:330px;font-weight:800;color:var(--watermark);letter-spacing:-12px;line-height:1;text-transform:uppercase;white-space:nowrap}
  .letterhead__footer{position:absolute;left:0;bottom:0;width:100%;height:140px;background:var(--gray);border-top:9px solid var(--orange);color:#fff;text-align:center;padding-top:38px;font-size:17px;line-height:22px}
  .letterhead__footer strong{font-weight:700}

  /* Labels */
  .piece-label{position:absolute;font-size:19px;color:var(--label);white-space:nowrap}
  .piece-label--vertical{left:842px;top:16px;writing-mode:vertical-rl}

  /* Cards */
  .card{position:absolute;left:794px;width:398px;height:232px;border-radius:14px;overflow:hidden}
  .card--front{top:198px;background:var(--paper);border:1px solid #cfcfcf;box-shadow:0 1px 3px rgba(0,0,0,.15)}
  .card--front .wordmark{position:absolute;left:22px;top:34px;font-size:44px}
  .card--front .tagline{position:absolute;left:23px;top:82px;font-size:8.5px}
  .card__divider{position:absolute;left:212px;top:28px;width:3px;height:62px;background:var(--orange)}
  .card--front .services{position:absolute;left:226px;top:30px;font-size:10px;line-height:14px}
  .card--front .services svg{width:9px;height:9px;margin-right:4px}
  .card__watermark{position:absolute;left:250px;top:96px;font-size:110px;font-weight:800;color:var(--watermark);letter-spacing:-4px;line-height:1;text-transform:uppercase}
  .card__person{position:absolute;right:110px;top:114px;text-align:left;color:var(--gray-dark)}
  .card__name{font-size:15px;font-weight:700;text-transform:uppercase}
  .card__role{font-size:8.5px;text-transform:uppercase;color:var(--gray-text)}
  .card__footer{position:absolute;left:0;bottom:0;width:100%;height:56px;background:var(--gray);border-top:4px solid var(--orange);color:#fff;text-align:center;font-size:11.5px;line-height:15px;padding-top:10px}

  .card--back{display:flex;flex-direction:column;justify-content:center;padding-left:84px}
  .card--back .wordmark{font-size:58px;color:#fff}
  .card--back .tagline{font-size:11px;color:#fff;margin-top:6px}
  .card--back .card__watermark{left:150px;top:40px;font-size:170px}
  .card--gray{top:508px;background:var(--gray-dark)}
  .card--gray .card__watermark{color:rgba(255,255,255,.07)}
  .card--orange{top:804px;background:linear-gradient(135deg,var(--orange-light),var(--orange))}
  .card--orange .card__watermark{color:rgba(255,255,255,.18)}
  .card--back .wordmark,.card--back .tagline{position:relative}
</style>
</head>
<body>

<section class="letterhead" aria-label="Papel timbrado">
  <div class="letterhead__top-band"></div>
  <div class="wordmark">Palkoro</div>
  <div class="tagline">Soluções em Tecnologia da Informação</div>
  <ul class="services">
    <li><svg viewBox="0 0 10 10"><path d="M1 5.5 4 8.5 9 1.5" fill="none" stroke="var(--orange)" stroke-width="2"/></svg>Serviços realizados</li>
    <li><svg viewBox="0 0 10 10"><path d="M1 5.5 4 8.5 9 1.5" fill="none" stroke="var(--orange)" stroke-width="2"/></svg>Serviços realizados</li>
    <li><svg viewBox="0 0 10 10"><path d="M1 5.5 4 8.5 9 1.5" fill="none" stroke="var(--orange)" stroke-width="2"/></svg>Serviços realizados</li>
    <li><svg viewBox="0 0 10 10"><path d="M1 5.5 4 8.5 9 1.5" fill="none" stroke="var(--orange)" stroke-width="2"/></svg>Serviços realizados</li>
  </ul>
  <div class="letterhead__watermark" aria-hidden="true">Palkoro</div>
  <footer class="letterhead__footer">
    Endereço | Rua Fulano de Tal | Bairro Cicrano de Tal | Cidade | Estado<br>
    <strong>Fone: (11) 4000-1234 | Fax: (11) 4000-1234 | contato@palkoro.com</strong>
  </footer>
</section>

<div class="piece-label piece-label--vertical">Timbrado</div>

<div class="piece-label" style="left:884px;top:172px">Cartão de Visita - Frente</div>
<section class="card card--front" aria-label="Cartão de visita, frente">
  <div class="card__watermark" aria-hidden="true">Palkoro</div>
  <div class="wordmark">Palkoro</div>
  <div class="tagline">Soluções em Tecnologia da Informação</div>
  <div class="card__divider"></div>
  <ul class="services">
    <li><svg viewBox="0 0 10 10"><path d="M1 5.5 4 8.5 9 1.5" fill="none" stroke="var(--orange)" stroke-width="2"/></svg>Serviços realizados</li>
    <li><svg viewBox="0 0 10 10"><path d="M1 5.5 4 8.5 9 1.5" fill="none" stroke="var(--orange)" stroke-width="2"/></svg>Serviços realizados</li>
    <li><svg viewBox="0 0 10 10"><path d="M1 5.5 4 8.5 9 1.5" fill="none" stroke="var(--orange)" stroke-width="2"/></svg>Serviços realizados</li>
    <li><svg viewBox="0 0 10 10"><path d="M1 5.5 4 8.5 9 1.5" fill="none" stroke="var(--orange)" stroke-width="2"/></svg>Serviços realizados</li>
  </ul>
  <div class="card__person">
    <div class="card__name">Renato Alves</div>
    <div class="card__role">Diretor Administrativo</div>
  </div>
  <footer class="card__footer">
    Endereço | Rua Fulano de Tal | Bairro Cicrano de Tal | Cidade | Estado<br>
    Fone: (11) 4000-1234 | Fax: (11) 4000-1234 | contato@palkoro.com
  </footer>
</section>

<div class="piece-label" style="left:856px;top:478px">Cartão de Visita - Verso Opção 1</div>
<section class="card card--back card--gray" aria-label="Cartão de visita, verso opção 1">
  <div class="card__watermark" aria-hidden="true">Palkoro</div>
  <div class="wordmark">Palkoro</div>
  <div class="tagline">Soluções em Tecnologia da Informação</div>
</section>

<div class="piece-label" style="left:856px;top:772px">Cartão de Visita - Verso Opção 2</div>
<section class="card card--back card--orange" aria-label="Cartão de visita, verso opção 2">
  <div class="card__watermark" aria-hidden="true">Palkoro</div>
  <div class="wordmark">Palkoro</div>
  <div class="tagline">Soluções em Tecnologia da Informação</div>
</section>

</body>
</html>
```